Civic Holdwell Business Card

We are looking to design new business cards for our company. We have two office locations and would like to have both full addresses on the card. Each address needs two lines for the building name and street address and a line or two for the city, state and zip code. There should be a place for 2-3 phone numbers. The addresses and phone numbers are at the bottom of this description. We also need a place to put our company website and one email address. Our logo is attached.
We would like the card to be two sided. The back of the card should have a blue background with some part of our logo design on it. We would like the full logo on the front of the card as well. The front of the card should have a white background with the blue logo. We are open to listing our addresses on the front or the back of the card. The person who designed our logo gave us an excellent business card idea that we really liked. I have attached a picture of his business card idea so that we can build off of it.
Addresses:
The Tanner Hall
2184 17th Street NW
Washington, DC 20007
Marlow Crest Tower
410 Dorsen Avenue #2215
Miami, FL 33131
Phone Numbers: (202) 555-0148
(202) 555-0193
Website: www.civicholdwell.example

```html
<!DOCTYPE html>
<html lang="en">
<head>
<meta charset="utf-8">
<title>Civic Holdwell Business Card</title>
<link rel="stylesheet" href="https://fonts.googleapis.com/css2?family=Lato:wght@400&display=swap">
<style>
  :root {
    --page: #ffffff;
    --backdrop-light: #f3f3f4;
    --backdrop-dark: #d9dadc;
    --card-white: #ffffff;
    --brand-blue: #2b3478;
    --card-edge: #d4d5d8;
  }
  * { box-sizing: border-box; margin: 0; padding: 0; }
  html, body {
    width: 1200px;
    height: 969px;
    overflow: hidden;
    background: var(--page);
    font-family: "Lato", sans-serif;
  }
  .backdrop {
    position: absolute;
    left: 24px;
    top: 24px;
    width: 1152px;
    height: 922px;
    background: radial-gradient(ellipse at 50% 45%, var(--backdrop-light) 0%, var(--backdrop-light) 35%, var(--backdrop-dark) 100%);
  }
  .card {
    position: absolute;
    left: 394px;
    width: 408px;
    height: 234px;
    border-radius: 16px;
    overflow: hidden;
    border: 1px solid var(--card-edge);
  }
  .card-front {
    top: 208px;
    background: var(--card-white);
  }
  .card-back {
    top: 525px;
    background: var(--brand-blue);
  }
  .brand {
    position: absolute;
    right: 22px;
    top: 96px;
    display: flex;
    align-items: center;
    gap: 6px;
  }
  .brand-square {
    width: 34px;
    height: 38px;
    background: var(--brand-blue);
    border-radius: 3px;
  }
  .brand-name {
    color: var(--brand-blue);
    font-size: 27px;
    font-weight: 400;
    letter-spacing: 0.5px;
    line-height: 1;
  }
  .front-web {
    position: absolute;
    right: 22px;
    top: 142px;
    color: var(--brand-blue);
    font-size: 11px;
    letter-spacing: 0.4px;
  }
  .back-panel {
    position: absolute;
    left: 0;
    top: 0;
    width: 209px;
    height: 100%;
    background: var(--card-white);
    border-top-right-radius: 22px;
  }
  .back-mark {
    position: absolute;
    left: 52px;
    top: 88px;
    width: 112px;
    height: 112px;
    background: var(--brand-blue);
    border-radius: 4px;
  }
  .contact {
    position: absolute;
    right: 22px;
    top: 20px;
    text-align: right;
    color: var(--card-white);
    font-size: 12px;
    line-height: 16px;
  }
  .contact-block + .contact-block { margin-top: 21px; }
</style>
</head>
<body>
  <div class="backdrop"></div>

  <section class="card card-front" aria-label="Card front">
    <div class="brand">
      <span class="brand-square"></span>
      <span class="brand-name">Civic Holdwell</span>
    </div>
    <p class="front-web">www.civicholdwell.example</p>
  </section>

  <section class="card card-back" aria-label="Card back">
    <div class="back-panel">
      <span class="back-mark"></span>
    </div>
    <div class="contact">
      <p class="contact-block">The Tanner Hall<br>2184 17th Street NW<br>Washington, DC 20007</p>
      <p class="contact-block">(202) 555-0148<br>(202) 555-0193<br>info@civicholdwell.example</p>
      <p class="contact-block">Marlow Crest Tower<br>410 Dorsen Avenue #2215<br>Miami, FL 33131</p>
    </div>
  </section>
</body>
</html>
```